Event Flyer - LGBT Camping Event

I have attached a poster I made (SampleFlyer.pdf) that has all the elements I want. Just don't like the layout and how things look. You can use any colors that make the poster work. I would like to incorporate the Campfire Gathering logo into the flyer (uploaded). You are welcome to grab elements from the event website to incorporate into your design (www.campfiregatheringidaho.org). I included a couple of pictures to possibly use too. Please include all 8 sponsors and the two hosts are the logos on the bottom of sample flyer - Prairie Fairness & Northern Trails Agency. The flyer size needs to be 12"Wide x 17" Tall. Here is a dropbox link to a possible image to use. https://lnk.example/7xQmTza

Please use the wording;

DON’T MISS this LGBT camping event!

Plan the highlight of your summer TODAY.

It’s almost time for the Rocky Mountain Region’s largest LGBT pride camping event: Campfire Gathering Idaho!
Join us August 8th-12th for 5 days of fun in a friendly, safe, LGBT affirming environment for everyone, from everywhere!

More Info or Register Online www.plainsjoy.org

Target Market(s)

LGBT Campers

Industry/Entity Type

Event

Colors

Designer to choose colors to be used in the design.

Requirements
Must have
• Must have text outlined in project description, Campfire Gathering logo, sponsor logos and host logos.

```html
<!DOCTYPE html>
<html lang="en">
<head>
<meta charset="utf-8">
<title>Campfire Gathering Idaho – Event Flyer</title>
<link rel="stylesheet" href="https://fonts.googleapis.com/css2?family=Fjalla+One&family=Pathway+Gothic+One&family=Josefin+Sans:wght@600&display=swap">
<style>
  :root {
    --page-bg: #e9e9e9;
    --green-top: #11904f;
    --green-mid: #0b6f3c;
    --green-deep: #075830;
    --hill: #064a28;
    --accent: #7dc242;
    --white: #ffffff;
    --soft-white: #eef3ef;
    --navy: #1d2a55;
    --host-blue: #1f5fa0;
    --photo-a: #3c6b4a;
    --photo-b: #6f8fa8;
    --photo-c: #8a4a3a;
  }
  * { margin: 0; padding: 0; box-sizing: border-box; }
  html, body { width: 1200px; height: 1200px; overflow: hidden; }
  body { background: var(--page-bg); position: relative; }

  .flyer {
    position: absolute; left: 200px; top: 43px;
    width: 800px; height: 1114px; overflow: hidden;
    background: linear-gradient(180deg, var(--green-top) 0%, var(--green-mid) 45%, var(--green-deep) 100%);
    color: var(--white);
    font-family: "Pathway Gothic One", sans-serif;
  }

  .headline {
    position: absolute; top: 40px; left: 0; width: 100%;
    text-align: center; font-family: "Fjalla One", sans-serif;
    font-size: 66px; line-height: 80px; text-transform: uppercase;
    text-shadow: 0 3px 6px rgba(0,0,0,.35);
  }

  .hero-photo {
    position: absolute; top: 212px; left: 0; width: 800px; height: 460px;
    background:
      radial-gradient(ellipse at 30% 55%, var(--photo-b) 0%, transparent 45%),
      radial-gradient(ellipse at 35% 80%, var(--photo-c) 0%, transparent 40%),
      linear-gradient(180deg, var(--green-mid) 0%, var(--photo-a) 50%, #2f4a3a 100%);
  }

  .event-mark {
    position: absolute; top: 392px; left: 470px; width: 300px; text-align: center;
    padding: 22px 0 12px;
    background: radial-gradient(ellipse at center, rgba(255,255,255,.92) 35%, rgba(255,255,255,0) 72%);
  }
  .event-mark .name {
    font-family: "Josefin Sans", sans-serif; font-weight: 600;
    font-size: 27px; color: var(--navy); letter-spacing: 1px; text-transform: uppercase;
  }
  .event-mark .tagline {
    font-family: "Josefin Sans", sans-serif; font-weight: 600;
    font-size: 11px; color: var(--navy); letter-spacing: 1px; text-transform: uppercase; margin-top: 2px;
  }

  .call-to-action {
    position: absolute; top: 515px; right: 32px; text-align: right;
    font-family: "Fjalla One", sans-serif; font-size: 68px; line-height: 78px;
    text-transform: uppercase; text-shadow: 0 3px 6px rgba(0,0,0,.45);
  }
  .call-to-action .hl { color: var(--accent); }

  .details {
    position: absolute; top: 700px; left: 0; width: 100%;
    text-align: center; font-size: 30px; line-height: 39.5px; text-transform: uppercase;
  }
  .details .hl { color: var(--accent); }

  .hills { position: absolute; left: 0; top: 880px; width: 800px; height: 234px; }

  .host {
    position: absolute; top: 878px; display: flex; align-items: center; gap: 8px;
    font-family: "Pathway Gothic One", sans-serif; font-size: 20px; text-transform: uppercase;
  }
  .host-trails { left: 36px; color: #f2d23a; }
  .host-trails .mark { width: 22px; height: 22px; border-radius: 50%; background: #f2d23a; }
  .host-fairness { right: 34px; color: var(--host-blue); font-size: 30px; }
  .host-fairness .mark { width: 24px; height: 24px; background: var(--host-blue); }

  .register {
    position: absolute; top: 890px; left: 0; width: 100%; text-align: center;
    color: var(--soft-white); font-size: 26px; line-height: 38px; text-transform: uppercase;
  }
  .register .url { letter-spacing: 7px; }

  .sponsor-label {
    position: absolute; top: 1004px; left: 37px; font-size: 22px; text-transform: uppercase; letter-spacing: 1px;
  }
  .sponsors {
    position: absolute; top: 1034px; left: 37px; width: 730px; height: 48px;
    display: flex; gap: 8px;
  }
  .sponsor {
    flex: 1; display: flex; align-items: center; justify-content: center; text-align: center;
    background: var(--soft-white); color: #333; font-size: 15px; line-height: 16px;
    text-transform: uppercase; padding: 0 4px;
  }
  .sponsor.dark { background: #111; color: var(--white); }
</style>
</head>
<body>
  <main class="flyer">
    <h1 class="headline">Don’t miss this<br>LGBT camping event!</h1>

    <div class="hero-photo" role="img" aria-label="Photo of two smiling men relaxing together outdoors on a grassy mountainside"></div>

    <div class="event-mark">
      <div class="name">Campfire Gathering</div>
      <div class="tagline">Idaho’s LGBT Camping Event</div>
    </div>

    <p class="call-to-action">Plan the <span class="hl">highlight</span><br>of your <span class="hl">summer</span> today</p>

    <p class="details">
      It’s almost time for the Rocky Mountain Region’s<br>
      largest LGBT pride camping event: <span class="hl">Campfire Gathering Idaho!</span><br>
      Join us <span class="hl">August 8th–12th</span> for 5 days of fun in a friendly, safe,<br>
      LGBT affirming environment for everyone, from everywhere!
    </p>

    <svg class="hills" viewBox="0 0 800 234" preserveAspectRatio="none" aria-hidden="true">
      <path d="M0 90 C60 60 110 40 170 70 C230 100 250 60 320 40 C380 25 420 70 470 95 C520 120 560 70 610 50 C660 30 700 70 740 100 C765 115 785 110 800 105 L800 234 L0 234 Z" fill="var(--hill)" opacity=".75"/>
    </svg>

    <div class="host host-trails"><span class="mark"></span>Northern Trails Agency</div>

    <p class="register">More info or register online<br><span class="url">www.plainsjoy.org</span></p>

    <div class="host host-fairness"><span class="mark"></span>Prairie Fairness</div>

    <p class="sponsor-label">Sponsored by</p>
    <div class="sponsors">
      <div class="sponsor">Riverbend Physio</div>
      <div class="sponsor">Maple’s Boise</div>
      <div class="sponsor">Open Peaks Alliance</div>
      <div class="sponsor">learnplains.org</div>
      <div class="sponsor dark">Vertex</div>
      <div class="sponsor dark">J’s Corner Shops</div>
      <div class="sponsor">Harlan Brooks</div>
    </div>
  </main>
</body>
</html>
```